Patient Fact sheets for medical conditions and treatments

Hi,

I need a new design for my patient fact sheets. I am moving from my current clinic and I am looking from a new look.

I have attached
1. a current Fact sheet
2. New home page to the website
3. New Logo.

They need to be single page and easily readable for patients.

The will be in both PDF and print form in the future.

Target Market(s)

Patients with chronic pain age 40+

Font styles to use
Serif

Requirements
Must have
• My logo, should be inline with design elements on the Front page provided.

Please use the same font as the Logo

```html
<!DOCTYPE html>
<html lang="en">
<head>
<meta charset="utf-8">
<title>Platelet Rich Plasma (PRP) Therapy – Patient Fact Sheet</title>
<link href="https://fonts.googleapis.com/css2?family=Cinzel:wght@400;600&family=Montserrat:wght@400;500;600&display=swap" rel="stylesheet">
<style>
  :root{
    --page-bg:#f3f3f3;
    --sheet:#ffffff;
    --teal:#17a2b8;
    --teal-tint:#d7e6e4;
    --gold:#f2be45;
    --ink:#2b2b2b;
    --disclaimer-bg:#ebebf0;
    --photo-a:#6d7071;
    --photo-b:#b9bcc2;
  }
  *{box-sizing:border-box;margin:0;padding:0}
  html,body{width:1200px;height:840px;overflow:hidden;background:var(--page-bg)}
  body{font-family:"Montserrat",sans-serif;color:var(--ink)}
  .sheet{position:absolute;left:303px;top:0;width:594px;height:840px;background:var(--sheet);overflow:hidden}

  .header-photo{position:absolute;left:0;top:0;width:594px;height:184px;
    background:
      radial-gradient(ellipse 120px 60px at 210px 170px,#f4efe6 0%,rgba(244,239,230,0) 100%),
      linear-gradient(115deg,rgba(230,200,70,0) 30%,rgba(236,196,70,.85) 40%,rgba(236,196,70,.25) 55%,rgba(236,196,70,0) 62%),
      linear-gradient(90deg,var(--photo-a) 0%,var(--photo-b) 55%,#c9ccd2 100%)}

  .brand{position:absolute;left:22px;top:44px;font-family:"Montserrat",sans-serif;font-weight:500;
    font-size:15px;line-height:18px;color:#1d1d1d;letter-spacing:.5px;text-transform:uppercase;white-space:nowrap}
  .social{position:absolute;top:16px;right:24px;display:flex;gap:8px}
  .social span{width:17px;height:17px;border-radius:4px;background:#2b66b1;display:block}

  .accent-bar{position:absolute;left:245px;top:52px;width:349px;height:21px;background:var(--gold)}
  .accent-bar::before{content:"";position:absolute;left:0;top:0;width:25px;height:21px;background:var(--teal)}

  .title{position:absolute;left:31px;top:102px;font-family:"Cinzel",serif;font-weight:600;font-size:27px;
    color:var(--teal);letter-spacing:.3px;white-space:nowrap}
  .rule{position:absolute;left:26px;top:177px;width:540px;height:1px;background:var(--gold)}

  .intro{position:absolute;left:25px;top:185px;width:544px;height:82px;background:var(--teal-tint);
    padding:5px 12px 0 4px;font-size:10px;line-height:12px;text-align:justify}
  .intro h2{font-size:10px;font-weight:600;text-transform:uppercase;color:#111;line-height:12px}

  .col{position:absolute;top:275px;font-size:10px;line-height:10.9px;text-align:justify}
  .col-left{left:25px;width:268px}
  .col-right{left:304px;width:267px;line-height:10.4px}
  .col h3{font-size:10.5px;font-weight:600;text-transform:uppercase;color:var(--teal);letter-spacing:.6px;
    line-height:12px;margin-bottom:11px;text-align:left}
  .col p{margin-bottom:12px}
  .col ul{list-style:none;margin:-8px 0 0}
  .col li{padding-left:8px;position:relative}
  .col li::before{content:"";position:absolute;left:1px;top:4px;width:3px;height:3px;border-radius:50%;background:var(--teal)}
  .treat-list{margin:0 !important;text-align:left}
  .tight{margin-bottom:0 !important;text-align:left}
  .results{margin-top:12px}

  .info-band{position:absolute;left:304px;top:594px;width:279px;height:11px;background:var(--gold)}
  .info-title{position:absolute;left:308px;top:612px;font-size:11px;font-weight:600;color:var(--teal);letter-spacing:.4px}
  .contact{position:absolute;left:308px;top:636px;width:285px;list-style:none;font-size:10px;line-height:11px}
  .contact li{display:flex;align-items:flex-start;margin-bottom:11px}
  .contact li.gap{margin-bottom:22px}
  .contact svg{width:13px;height:13px;flex:none;margin:0 38px 0 8px;fill:var(--teal)}

  .disclaimer{position:absolute;left:13px;top:744px;width:570px;height:92px;background:var(--disclaimer-bg);
    padding:4px 11px 0 11px;font-size:10px;line-height:12.1px;text-align:justify}
  .disclaimer h2{font-size:10px;font-weight:500;color:var(--teal);text-transform:uppercase;line-height:12px}
</style>
</head>
<body>
<article class="sheet">
  <div class="header-photo" role="img" aria-label="Photo of a gloved hand holding a test tube of golden plasma"></div>
  <div class="brand">Dr Alan Reeve</div>
  <div class="social" aria-hidden="true"><span></span><span></span><span></span></div>
  <div class="accent-bar"></div>
  <h1 class="title">Platelet Rich Plasma (PRP) Therapy</h1>
  <div class="rule"></div>

  <section class="intro">
    <h2>What is PRP?</h2>
    <p>Platelet-Rich Plasma (PRP) is concentrated platelets and white blood cells derived from your own blood. Platelet Rich Plasma Injection Therapy (PRP therapy), is a growing treatment approach for soft tissue injuries including tendon, muscle and ligaments. It is also showing good results for mild to moderate osteo-arthritis. While this approach has been used overseas for many years, it’s fairly new to Australia in the treatment of musculoskeletal and orthopaedic conditions.</p>
  </section>

  <section class="col col-left">
    <h3>How does PRP work?</h3>
    <p>Some tissues in the body have a poor blood supply or respond poorly to excessive load, ultimately failing to heal naturally. While some of our primary treatment such as physiotherapy, massage, biomechanical correction and other forms of treatment are used to treat these soft tissue injuries, sometimes the body fails to respond. PRP therapy utilises the healing properties in blood to allow a healing reaction to occur in a tissue that’s not healing on its own. Our blood has small granules called ‘platelets’, which contain special growth factors that when released, allow stem cells in the particular tissue to ‘switch’ on and cause new tissue to be created and heal the injured area. Take the example of achilles tendinopathy. If the achilles is painful, thickened and not responding to rehabilitation, then the sports physician will inject the PRP into the achilles which will cause the tendon cells (tenocytes/fibroblasts) to create new achilles collagen to strengthen the achilles. White blood cells also enter the area to mop up any achilles tissue that may have been damaged due to the ongoing pain and thickening in the area.</p>
    <h3>Role of platelets &amp; growth factors</h3>
    <p>PRP contains highly concentrated platelets. Platelets have been identified to secrete growth factors, which are known to play a role in:</p>
    <ul>
      <li>increasing tissue vascularity and increasing the rate of epithelial tissue production (wound healing)</li>
      <li>attracting other cells that fight infection</li>
      <li>acting as a seal during closures</li>
      <li>providing an immediate surgical hemostatic agent (reduction of bleeding)</li>
      <li>osteogenesis (bone regeneration and repair)</li>
    </ul>
  </section>

  <section class="col col-right">
    <h3>What can PRP treat?</h3>
    <p class="tight">PRP therapy can be used for:</p>
    <ul class="treat-list">
      <li>orthopedic surgery</li>
      <li>cardiac surgery</li>
      <li>plastic and cosmetic surgery</li>
      <li>ear, nose, throat (ENT) surgery</li>
      <li>oral maxillofacial surgery</li>
      <li>neurosurgery</li>
      <li>vascular surgery</li>
      <li>wound healing</li>
      <li>burn care.</li>
    </ul>
    <p class="tight">Ask your doctor whether platelet rich plasma is appropriate for your surgical procedure</p>
    <h3 class="results">What are the expected results of PRP?</h3>
    <p>Because the goal of PRP therapy is to resolve pain through healing, it could prove to have lasting results. Initial improvement may be seen within a few weeks, gradually increasing as the healing progresses. Research studies and clinical practice have shown PRP therapy to be very effective at relieving pain and returning patients to their normal lives. The need for surgery can also be greatly reduced by treating injured tissues before the damage progresses and the condition is irreversible.</p>
  </section>

  <div class="info-band"></div>
  <h2 class="info-title">For more information</h2>
  <ul class="contact">
    <li><svg viewBox="0 0 24 24"><path d="M12 2a7 7 0 0 0-7 7c0 5 7 13 7 13s7-8 7-13a7 7 0 0 0-7-7zm0 9.5A2.5 2.5 0 1 1 12 6.5a2.5 2.5 0 0 1 0 5z"/></svg><span>Harbour Pain Clinic Bayview House, Level 1,<br>48 Harbour Street, Seacliff VIC 3190</span></li>
    <li class="gap"><svg viewBox="0 0 24 24"><path d="M7 1h10a2 2 0 0 1 2 2v18a2 2 0 0 1-2 2H7a2 2 0 0 1-2-2V3a2 2 0 0 1 2-2zm0 3v15h10V4z"/></svg><span>03 9000 4821 - 03 9000 4822</span></li>
    <li><svg viewBox="0 0 24 24"><path d="M2 5h20v14H2zm2 2v.5l8 5 8-5V7z"/></svg><span>info@harbourpain.example</span></li>
    <li><svg viewBox="0 0 24 24"><path d="M12 2a10 10 0 1 0 0 20 10 10 0 0 0 0-20zm-1 17.9A8 8 0 0 1 4.1 10L9 15v1a2 2 0 0 0 2 2zm6.9-2.5A2 2 0 0 0 16 16h-1v-3a1 1 0 0 0-1-1H8v-2h2a1 1 0 0 0 1-1V7h2a2 2 0 0 0 2-2v-.4a8 8 0 0 1 2.9 12.8z"/></svg><span>harbourpain.example</span></li>
  </ul>

  <section class="disclaimer">
    <h2>Disclaimer</h2>
    <p>Please note the contents contained in this Patient Fact Sheet are not intended as a substitute for your own independent health professional’s advice, diagnosis or treatment. At Harbour Pain Clinic, we assess every patient’s condition individually. As leaders in pain intervention, we aim to provide advanced, innovative, and evidence-based treatments tailored to suit each patient. As such, recommended treatments and their outcomes will vary from patient to patient. If you would like to find out whether our treatments are suitable for your specific condition, please speak to one of our doctors at the time of your consultation.</p>
  </section>
</article>
</body>
</html>
```